Packaging design for high end, natural skin care line needed

Marisa Holloway Beauty needs a label design. It is a new skin care line I am launching.
For years my line Pure Meadow Beauty was quite popular and featured in several magazines, but for personal reasons had to be shut down. Now I am launching a new line featuring PMB's top selling products, but focused solely on skin care more so than cosmetics. All products will still be handmade, but the line should still look professional-something worthy of a Fresh Larder shelf!
I am branding it with my name, as I am often quoted in articles related to gluten in beauty products, so Marisa Holloway and beauty are key words.
The key products will be facial and body serums which are packaged in .5oz., 1oz. and larger amber glass bottles with black dropper tops, I will include pictures below. For dimensions, the labels can be any size that you think will work best, but need to at the least fit the 1oz. bottle, dimensions shown here http://www.brightvialshop.example/amber-glass-round-vial/p/QX7T-52/
I loved the former PMB logo, but for Marisa Holloway Beauty I am looking for something more personal, more apothecary-like, and probably less colorful.
The line will be small, just a handful of products, but luxe, rich.
I am attaching photos of Pure Meadow Beauty's packaging for your reference.
Thanks much!!
Updates

Hi Everyone! Thank you for your submissions! Please see the links I provided in the brief, I really am looking for something more technical looking, like an apothecary. And want black text on a white background, not a black background, and nothing flowery.
Thank you all!!
Marisa

Target Market(s)

My clients are primarily women of all ages, but with more of a skin care focus, and no longer a cosmetic one, I would also like to appeal to a male audience. My clients are health conscious, gluten-free, natural, paleo, or vegan, etc. Target age is probably 25-55. Products are a bit high end, priced $45-65.

Industry/Entity Type

Cosmetics

Requirements
Must have
• It must at least say Marisa Holloway, or can say Marisa Holloway Beauty, but "Beauty" is not necessary. And capitalization is open, try whatever you think serves the brand. Likely slogans or taglines that can be included but are not essential: Care for your skin. Love and care for your skin. Handmade with love in the USA. Handmade in the USA. Think modern day apothecary. Small batch scotch. Something fine, but custom, handmade.
Nice to have
• I like the aesthetic of Tolmi Skin Care a bit http://www.rosalindtarvey.example.au/
And of Dorian Pelku as shown here http://www.pinboardly.example/pin/584203917660218447/
Also of something like this that is even customizable http://www.pinboardly.example/pin/76920418835102734/
Every product is handmade in small batches, with fine ingredients, a moderate price point of around $45-$65. And I will likely begin making custom orders. So there could be a space to say when it was made, or for whom. I would like to keep the colors classic though, I probably want to stay away from the bright pink on this one.
Should not have
• As I mentioned, probably want to stay away from a lot of color. I like black vs. gray for the text, as it will show up better in editorials. I must look good, but also photograph well. Thanks!

```html
<!DOCTYPE html>
<html lang="en">
<head>
<meta charset="utf-8">
<title>Marisa Holloway Beauty — Label</title>
<link rel="stylesheet" href="https://fonts.googleapis.com/css2?family=Courier+Prime&family=Noto+Sans:wght@400&family=Noto+Sans+Mono:wght@400&display=swap">
<style>
  :root {
    --teal: #55aab4;
    --ink: #444444;
    --paper: #fdfdfd;
    --page: #ffffff;
  }
  html, body {
    margin: 0;
    padding: 0;
    width: 1200px;
    height: 1200px;
    overflow: hidden;
    background: var(--page);
  }
  .label {
    position: absolute;
    left: 28px;
    top: 248px;
    width: 1105px;
    height: 630px;
    background: var(--paper);
    box-shadow: 0 0 0 1px #eeeeee;
  }
  .band {
    position: absolute;
    left: 0;
    width: 100%;
    height: 16px;
    background: var(--teal);
  }
  .band--top { top: 0; }
  .band--bottom { bottom: 0; }
  .brand {
    position: absolute;
    top: 150px;
    left: 0;
    width: 100%;
    text-align: center;
  }
  .brand__name {
    margin: 0;
    font-family: "Noto Sans", sans-serif;
    font-weight: 400;
    font-size: 52px;
    line-height: 68px;
    letter-spacing: 1px;
    color: var(--ink);
  }
  .brand__tag {
    margin: 0;
    font-family: "Noto Sans Mono", monospace;
    font-size: 32px;
    line-height: 40px;
    letter-spacing: 4px;
    color: var(--teal);
  }
  .origin {
    position: absolute;
    left: 443px;
    top: 522px;
    font-family: "Courier Prime", monospace;
    font-size: 18px;
    letter-spacing: 1px;
    color: var(--ink);
  }
  .origin__leaf {
    position: absolute;
    left: 667px;
    top: 524px;
    width: 86px;
    height: 64px;
    border-radius: 50% 50% 50% 50% / 60% 60% 40% 40%;
    background: radial-gradient(ellipse at 40% 40%, #6fb8c0, #55aab4 60%, rgba(85,170,180,0.3));
    transform: rotate(12deg);
  }
  .batch {
    position: absolute;
    left: 962px;
    top: 39px;
    width: 127px;
    height: 532px;
  }
  .batch text {
    font-family: "Courier Prime", monospace;
    font-size: 28px;
    letter-spacing: 3px;
    fill: var(--ink);
  }
</style>
</head>
<body>
  <main class="label">
    <div class="band band--top"></div>

    <header class="brand">
      <h1 class="brand__name">MARISA HOLLOWAY</h1>
      <p class="brand__tag">beauty</p>
    </header>

    <p class="origin" style="margin:0">Handmade in the USA</p>
    <div class="origin__leaf" role="img" aria-label="Small teal leaf illustration"></div>

    <svg class="batch" viewBox="0 0 127 532" aria-label="Batch details">
      <rect x="1" y="1" width="125" height="530" fill="none" stroke="#444444" stroke-width="2"/>
      <line x1="64" y1="13" x2="64" y2="519" stroke="#444444" stroke-width="2"/>
      <text transform="translate(47 510) rotate(-90)">Made: 15.01.2014</text>
      <text transform="translate(107 510) rotate(-90)">For: Helena Marsh</text>
    </svg>

    <div class="band band--bottom"></div>
  </main>
</body>
</html>
```